Revamp our website

Our website needs a bit of a makeover as it is quite simple and not very interactive. Specific pages we would like to see renewed is the home page (www.lunarkpower.com.au) , solutions top page (https://www.lunarkpower.com.au/solutions/) and a detailed solution page (https://www.lunarkpower.com.au/tesko-retail-final/)

The colour data lines are key to our branding and must be used (happy to see them being used in different ways).

```html
<!DOCTYPE html>
<html lang="en">
<head>
<meta charset="utf-8">
<title>Lunark – Home</title>
<link href="https://fonts.googleapis.com/css2?family=Poppins:wght@400;500;600;700&family=Open+Sans:ital,wght@0,400;0,600;1,400&display=swap" rel="stylesheet">
<style>
:root{
  --red:#d0073f;
  --red-deep:#b8053a;
  --pink:#e23a66;
  --ink:#1d1d1d;
  --body:#3c3c3c;
  --grey-bg:#ececec;
  --grey-light:#f4f4f4;
  --dark:#2a2727;
  --white:#ffffff;
}
*{margin:0;padding:0;box-sizing:border-box}
html,body{width:1200px;height:3377px;overflow:hidden;background:var(--white)}
body{position:relative;font-family:"Open Sans",Arial,sans-serif;color:var(--body)}
.abs{position:absolute}
h1,h2,h3,.heading{font-family:"Poppins",Arial,sans-serif;color:var(--ink)}
.btn{position:absolute;display:flex;align-items:center;justify-content:center;border:2px solid var(--red);border-radius:40px;color:var(--red);font-family:"Poppins",Arial,sans-serif;font-weight:600;background:var(--white)}

/* hero */
.hero-photo{left:0;top:0;width:1200px;height:720px;background:linear-gradient(135deg,#c93a5d 0%,#d84a6c 45%,#b92c52 100%)}
.nav{top:22px;left:0;width:1200px;height:70px}
.brand{left:160px;top:22px;font-family:"Poppins",Arial,sans-serif;font-weight:600;font-size:48px;color:var(--white);line-height:1}
.nav-links{left:430px;top:40px;display:flex;gap:38px;font-family:"Poppins",Arial,sans-serif;font-size:18px;color:var(--white)}
.nav-cta{left:884px;top:32px;width:152px;height:46px;border-radius:24px;background:var(--white);color:var(--red);font-family:"Poppins",Arial,sans-serif;font-size:18px;display:flex;align-items:center;justify-content:center}
.hero-title{left:0;top:276px;width:1200px;text-align:center;font-size:54px;font-weight:600;color:var(--white)}
.hero-sub{left:0;top:346px;width:1200px;text-align:center;font-size:25px;line-height:28px;color:var(--white);font-family:"Open Sans",Arial,sans-serif}
.dots{left:550px;top:602px;display:flex;gap:6px;align-items:center}
.dots span{width:9px;height:9px;border-radius:50%;background:rgba(255,255,255,.6)}
.dots span.on{background:var(--white)}
.dots i{width:16px;height:16px;border-radius:50%;background:var(--white);display:block}

/* intro */
.intro{left:0;top:700px;width:1200px;height:612px;background:linear-gradient(#fff,#f1f1f1)}
.intro-title{left:0;top:742px;width:1200px;text-align:center;font-size:32px;font-weight:600}
.intro-text{left:0;top:792px;width:1200px;text-align:center;font-size:17px;line-height:23px;color:var(--body)}
.card{position:absolute;top:884px;width:272px;height:346px;background:var(--white);border:2px solid #d3d3d3;border-radius:64px;text-align:center}
.card h3{font-size:23px;font-weight:500;line-height:24px;margin-top:166px}
.card p{font-size:12.5px;line-height:19px;color:var(--body);padding:0 28px;margin-top:10px}
.card .btn{left:73px;width:134px;height:40px;font-size:13px}
.card svg{position:absolute;left:96px;top:44px}

/* what we do */
.what-photo{left:0;top:1312px;width:585px;height:440px;background:linear-gradient(120deg,#c9c3bd,#a98069 45%,#e8e2d8)}
.what-title{left:618px;top:1418px;font-size:30px;font-weight:600}
.what-text{left:618px;top:1476px;width:420px;font-size:15.5px;line-height:22px}
.what-text p+p{margin-top:21px}

/* products */
.products{left:0;top:1822px;width:1200px;height:500px;background:var(--grey-bg)}
.products-title{left:0;top:1856px;width:1200px;text-align:center;font-size:30px;font-weight:600}
.product-name{left:200px;top:1944px;font-size:30px;font-weight:400;color:var(--red);font-family:"Poppins",Arial,sans-serif}
.product-text{left:200px;top:1992px;width:400px;font-size:15.5px;line-height:25px}
.product-art{left:612px;top:1918px;width:400px;height:252px;background:linear-gradient(135deg,#dfe6ea,#c7d3db 60%,#e9ecee);border-radius:12px}

/* philosophy */
.phil-title{left:0;top:2356px;width:1200px;text-align:center;font-size:30px;font-weight:600}
.quote-ring{left:310px;top:2422px;width:608px;height:212px;border:4px solid #8a8a8a;border-radius:106px}
.quote{left:328px;top:2434px;width:572px;height:188px;border-radius:94px;background:var(--red);color:var(--white);text-align:center}
.quote .mark{font-family:"Poppins",Arial,sans-serif;font-size:52px;line-height:40px;margin-top:26px;font-weight:700}
.quote p{font-style:italic;font-size:17.5px;line-height:22px;margin-top:6px;padding:0 90px}
.quote .author{font-style:normal;font-size:16px;margin-top:16px}

/* footer */
.footer-photo{left:0;top:2712px;width:1200px;height:590px;background:linear-gradient(110deg,#3a3433,#5a4d48 50%,#2f2a29)}
.mail{left:158px;top:2804px;width:456px;height:372px;background:var(--red)}
.mail h3{position:absolute;left:56px;top:38px;color:var(--white);font-size:29px;font-weight:400}
.mail label{position:absolute;left:54px;font-family:"Poppins",Arial,sans-serif;font-size:15px;color:var(--white);font-weight:500}
.mail .field{position:absolute;left:54px;width:370px;height:44px;border:1.5px solid rgba(255,255,255,.85)}
.mail .field svg{position:absolute;left:14px;top:12px}
.join{left:56px;top:276px;width:170px;height:52px;border-radius:28px;background:#3e0a17;color:var(--white);font-family:"Poppins",Arial,sans-serif;font-weight:600;font-size:17px;display:flex;align-items:center;justify-content:center}
.contact-title{left:686px;top:2814px;font-size:33px;font-weight:600;color:var(--white)}
.contact-item{left:738px;color:var(--white);font-family:"Poppins",Arial,sans-serif;font-size:17px;line-height:23px}
.contact-item b{font-weight:500;font-size:15px}
.socials{left:702px;top:3084px;display:flex;gap:11px}
.socials span{width:36px;height:36px;border:2px solid var(--white);border-radius:50%}
.copyright{left:0;top:3328px;width:1200px;text-align:center;font-size:13.5px;color:#555}
</style>
</head>
<body>

<!-- Hero -->
<div class="abs hero-photo" role="img" aria-label="Point-of-sale terminal and receipt printer under a red colour wash"></div>
<svg class="abs" style="left:0;top:600px" width="1200" height="130" viewBox="0 0 1200 130">
  <polygon points="0,30 0,130 1200,130 1200,62" fill="#e3e3e3"/>
  <polygon points="0,110 560,66 0,66" fill="var(--red)" opacity="0"/>
  <polygon points="0,62 1200,62 1200,75 0,120" fill="#ffffff"/>
  <polygon points="0,106 540,64 0,64" fill="#ed5a80" opacity=".9"/>
  <polygon points="0,114 620,64 820,64" fill="var(--red)"/>
</svg>
<div class="abs brand">lunark</div>
<nav class="abs nav-links"><span>Solutions</span><span>Products</span><span>News</span><span>About Us</span></nav>
<div class="abs nav-cta">Get in touch</div>
<h1 class="abs hero-title">Fortune favours the Lunark</h1>
<div class="abs hero-sub">Class aptent taciti sociosqu ad litora torquent per<br>conubia nostra per inceptos hymenaeos</div>
<div class="abs dots"><i></i><span class="on"></span><span></span><span></span><span></span><i></i></div>

<!-- Intro -->
<section class="abs intro"></section>
<svg class="abs" style="left:0;top:666px" width="1200" height="50" viewBox="0 0 1200 50"><polygon points="0,50 560,4 0,4" fill="#fff"/></svg>
<h2 class="abs intro-title">We’re here for you.</h2>
<p class="abs intro-text">Specialising in the Australian Utilities sector, we are driven to improve your operations<br>and customer experience through intelligent software.</p>

<svg class="abs" style="left:146px;top:870px" width="120" height="180" viewBox="0 0 120 180"><path d="M100,0 A100,100 0 0 0 0,100 L0,170 L100,170 Z" fill="var(--red)"/></svg>
<svg class="abs" style="left:990px;top:1040px" width="80" height="200" viewBox="0 0 80 200"><path d="M0,20 Q70,10 74,80 L60,170 L0,190 Z" fill="var(--pink)"/><path d="M20,40 Q60,70 40,190 L0,200 Z" fill="var(--red)"/></svg>

<article class="card" style="left:169px">
  <svg width="80" height="80" viewBox="0 0 80 80" fill="none" stroke="var(--red)" stroke-width="2.4"><rect x="6" y="8" width="68" height="46" rx="3"/><line x1="30" y1="54" x2="26" y2="68"/><line x1="50" y1="54" x2="54" y2="68"/><line x1="20" y1="70" x2="60" y2="70"/><rect x="32" y="18" width="34" height="14"/><line x1="32" y1="40" x2="66" y2="40"/><circle cx="18" cy="28" r="8"/></svg>
  <h3>Retail</h3>
  <p>Class aptent taciti sociosqu ad litora torquent per conubia nostra per inceptos hymenaeos</p>
  <div class="btn" style="top:274px">Learn More</div>
</article>
<article class="card" style="left:468px">
  <svg width="80" height="80" viewBox="0 0 80 80" fill="none" stroke="var(--red)" stroke-width="2.4"><circle cx="40" cy="40" r="36"/><circle cx="40" cy="40" r="27"/><line x1="40" y1="40" x2="54" y2="24"/><circle cx="40" cy="40" r="4"/><rect x="30" y="54" width="20" height="8" rx="2"/></svg>
  <h3>Metering Services</h3>
  <p>Class aptent taciti sociosqu ad litora torquent per conubia nostra per inceptos hymenaeos</p>
  <div class="btn" style="top:274px">Learn More</div>
</article>
<article class="card" style="left:765px">
  <svg width="80" height="80" viewBox="0 0 80 80" fill="none" stroke="var(--red)" stroke-width="2.4"><rect x="30" y="30" width="20" height="20"/><line x1="40" y1="6" x2="40" y2="30"/><line x1="40" y1="50" x2="40" y2="74"/><line x1="6" y1="40" x2="30" y2="40"/><line x1="50" y1="40" x2="74" y2="40"/><path d="M20,8 L20,24 L30,32 M60,8 L60,24 L50,32 M20,72 L20,56 L30,48 M60,72 L60,56 L50,48"/><circle cx="20" cy="6" r="3"/><circle cx="60" cy="6" r="3"/><circle cx="20" cy="74" r="3"/><circle cx="60" cy="74" r="3"/></svg>
  <h3>Distribution &amp;<br>Transmission</h3>
  <p>Class aptent taciti sociosqu ad litora torquent per conubia nostra</p>
  <div class="btn" style="top:272px">Learn More</div>
</article>

<!-- What we do -->
<svg class="abs" style="left:0;top:1290px" width="1200" height="70" viewBox="0 0 1200 70"><polygon points="760,20 1200,20 1200,70" fill="#f08aa5"/><polygon points="840,20 1200,10 1200,42" fill="var(--red)"/></svg>
<div class="abs what-photo" role="img" aria-label="Two colleagues working together at a desktop computer in a bright office"></div>
<svg class="abs" style="left:0;top:1740px" width="1200" height="90" viewBox="0 0 1200 90"><polygon points="0,30 1200,54 1200,90 0,90" fill="var(--grey-bg)"/><polygon points="0,10 700,40 0,60" fill="var(--red)"/><polygon points="0,0 340,24 0,20" fill="var(--pink)"/></svg>
<h2 class="abs what-title">What we do</h2>
<div class="abs what-text"><p>At Lunark™, we develop software solutions that are specifically designed for the Australian Utilities sector.</p><p>Founded by two industry leaders 15 years ago, we are about making the lives easier for those who work so hard to meet growing business and consumer demands.</p></div>
<div class="btn" style="left:618px;top:1642px;width:182px;height:54px;font-size:18px">Learn More</div>

<!-- Products -->
<section class="abs products"></section>
<h2 class="abs products-title">Our Products</h2>
<svg class="abs" style="left:120px;top:2036px" width="42" height="30" viewBox="0 0 42 30" fill="none" stroke="#555" stroke-width="3"><path d="M40,15 H4 M16,3 L4,15 L16,27"/></svg>
<svg class="abs" style="left:1032px;top:2036px" width="42" height="30" viewBox="0 0 42 30" fill="none" stroke="#555" stroke-width="3"><path d="M2,15 H38 M26,3 L38,15 L26,27"/></svg>
<div class="abs product-name">Billing</div>
<p class="abs product-text">Improve and automate your number one business process, no matter how flexible or complex the billing arrangements may be. Our powerful billing engines are designed to address the unique challenge you face in the Utilities industry, whilst remaining flexible to market change and your own business growth.</p>
<div class="btn" style="left:202px;top:2162px;width:168px;height:52px;font-size:18px">Learn More</div>
<div class="abs product-art" role="img" aria-label="Illustration of a laptop showing a bill, a payment card and a customer support agent"></div>
<svg class="abs" style="left:0;top:2270px" width="1200" height="60" viewBox="0 0 1200 60"><polygon points="0,52 1200,52 1200,60 0,60" fill="#fff"/><polygon points="820,20 1200,6 1200,52" fill="var(--red)"/><polygon points="1200,52 640,52 1200,30" fill="#fff"/></svg>

<!-- Philosophy -->
<h2 class="abs phil-title">Our Lunark Philosophy</h2>
<svg class="abs" style="left:220px;top:2516px" width="42" height="30" viewBox="0 0 42 30" fill="none" stroke="#555" stroke-width="3"><path d="M40,15 H4 M16,3 L4,15 L16,27"/></svg>
<svg class="abs" style="left:960px;top:2516px" width="42" height="30" viewBox="0 0 42 30" fill="none" stroke="#555" stroke-width="3"><path d="M2,15 H38 M26,3 L38,15 L26,27"/></svg>
<div class="abs quote-ring"></div>
<blockquote class="abs quote">
  <div class="mark">“</div>
  <p>Maintaining a thirst for knowledge, so that we can make sure our clients evolve alongside their customers.</p>
  <p class="author">By Author Name</p>
</blockquote>

<!-- Footer -->
<div class="abs footer-photo" role="img" aria-label="Team gathered around a table in a busy office, darkened"></div>
<svg class="abs" style="left:0;top:2700px" width="1200" height="40" viewBox="0 0 1200 40"><polygon points="0,0 1200,0 1200,10 0,40" fill="#fff"/></svg>
<form class="abs mail">
  <h3>Join Our Mailing List</h3>
  <label style="top:104px">NAME</label>
  <div class="field" style="top:130px"><svg width="18" height="18" viewBox="0 0 18 18" fill="none" stroke="#fff" stroke-width="1.5"><circle cx="9" cy="6" r="4"/><path d="M2,17 Q9,8 16,17 Z"/></svg></div>
  <label style="top:188px">EMAIL</label>
  <div class="field" style="top:214px"><svg width="20" height="16" viewBox="0 0 20 16" fill="none" stroke="#fff" stroke-width="1.5"><rect x="1" y="2" width="18" height="12"/><path d="M1,2 L10,9 L19,2"/></svg></div>
  <div class="abs join">JOIN NOW</div>
</form>
<h2 class="abs contact-title">Contact Us</h2>
<svg class="abs" style="left:688px;top:2896px" width="34" height="42" viewBox="0 0 34 42" fill="none" stroke="#fff" stroke-width="2"><path d="M17,38 C6,24 4,18 4,14 A13,13 0 0 1 30,14 C30,18 28,24 17,38 Z"/><circle cx="17" cy="14" r="5"/><ellipse cx="17" cy="38" rx="12" ry="3"/></svg>
<div class="abs contact-item" style="top:2890px"><b>ADDRESS</b><br>42 Wattle Parade<br>Kew Heights VIC 3102 Australia</div>
<svg class="abs" style="left:690px;top:3004px" width="36" height="36" viewBox="0 0 36 36" fill="none" stroke="#fff" stroke-width="2"><path d="M8,3 L14,3 L17,11 L13,14 C15,19 18,22 23,24 L26,20 L34,23 L34,29 C34,32 31,34 28,34 C14,32 4,22 3,8 C3,5 5,3 8,3 Z"/></svg>
<div class="abs contact-item" style="top:3000px"><b>PHONE NUMBER</b><br>+61 3 9012 4480</div>
<div class="abs socials"><span></span><span></span><span></span><span></span><span></span></div>

<p class="abs copyright">Copyright 2018 Lunark Power Pty Ltd ACN 204 318 576.</p>

</body>
</html>
```